Develop a Microsoft Word Add-In

I'd like an add-in developed for Microsoft Word (2013 & 2007 a must, ideally supporting 2007 & 2003), coded in C# using the standard visual studio tools for office libraries. Ideally I'd like a git / mercurial repo with the full source commit history.

The most basic version of the add-in needs to:
- Retrieve some JSON data from a URL, [url removed, login to view]
- Present a list of the keys in a pop-out or docked window in the main Word window.

e.g.

name
address
cars
-- make
-- age

- Allow a user to drag and drop the keys from the pop-out/docked window into the main document and insert the key text where dropped.

- Finally a bonus would be to be able to drag the cars array key onto the document and have a table created with headers of the internal keys (make & age), and a single row with the first set of values.

e.g.
-----------------
| Make | Age |
| KVR| 4 |
-----------------

This may well lead into more development in the future as I'm keen on building out more functionality.

Please get in touch if you have need clarification or have any questions.

Thanks!

```html
<!DOCTYPE html>
<html lang="en">
<head>
<meta charset="utf-8">
<title>Json To Doc Importer</title>
<link rel="stylesheet" href="https://fonts.googleapis.com/css2?family=Noto+Sans:wght@400;600&family=Caladea:ital,wght@0,400;0,700;1,400&family=Carlito:ital,wght@0,400;0,700;1,400&display=swap">
<style>
  :root {
    --titlebar: #dfe9f6;
    --ribbon-top: #f7f9fc;
    --ribbon-bottom: #dde6f2;
    --ribbon-line: #b8c7da;
    --group-label: #3e4e66;
    --workspace: #d7dfe9;
    --page: #ffffff;
    --page-edge: #9aa6b6;
    --pane: #e6ebf2;
    --pane-line: #a9b6c7;
    --text: #1e1e1e;
    --heading-blue: #4f6f9c;
    --title-blue: #17365d;
    --subtitle-blue: #4f81bd;
    --subtle: #808080;
    --link-blue: #1f37d8;
    --tree-line: #8a8a8a;
    --help-blue: #2f6fc4;
  }
  * { box-sizing: border-box; margin: 0; padding: 0; }
  html, body { width: 1115px; height: 1200px; overflow: hidden; background: var(--workspace); }
  .stage {
    position: absolute; left: 0; top: 0;
    width: 539px; height: 580px;
    transform: scale(2.0686); transform-origin: 0 0;
    font-family: "Noto Sans", sans-serif; font-size: 10.5px; color: var(--text);
    background: var(--workspace); overflow: hidden;
  }
  .abs { position: absolute; }

  .titlebar { left: 0; top: 0; width: 539px; height: 31px;
    background: linear-gradient(#eef4fb, var(--titlebar)); border-bottom: 1px solid #c9d6e6; }

  .ribbon { left: 0; top: 31px; width: 539px; height: 88px;
    background: linear-gradient(var(--ribbon-top), var(--ribbon-bottom));
    border-bottom: 1px solid var(--ribbon-line); }
  .style-tile { top: 8px; width: 70px; text-align: center; white-space: nowrap; overflow: hidden; }
  .style-sample { height: 36px; line-height: 40px; font-family: "Carlito", sans-serif; }
  .style-name { font-size: 11px; line-height: 16px; }
  .sample-h1 { font-family: "Caladea", serif; font-weight: 700; font-size: 17px; color: var(--heading-blue); }
  .sample-h2 { font-family: "Caladea", serif; font-weight: 700; font-size: 15px; color: var(--heading-blue); }
  .sample-title { font-family: "Caladea", serif; font-size: 31px; color: var(--title-blue); line-height: 34px; }
  .sample-subtitle { font-family: "Caladea", serif; font-style: italic; font-size: 14px; color: var(--subtitle-blue); letter-spacing: .5px; }
  .sample-subtle { font-style: italic; font-size: 13px; color: var(--subtle); }
  .gallery-scroll { left: 332px; top: 9px; width: 16px; height: 58px; border: 1px solid #b7c4d6;
    background: linear-gradient(#fbfcfe, #e4ebf4); }
  .group-label { top: 72px; font-size: 11px; color: var(--group-label); text-align: center; }
  .group-divider { top: 4px; width: 1px; height: 80px; background: #c3cfdf; }
  .edit-cmd { left: 410px; font-size: 11px; display: flex; align-items: center; gap: 4px; }

  .page { left: 0; top: 148px; width: 190px; height: 440px; background: var(--page);
    border-right: 1px solid var(--page-edge); border-top: 1px solid var(--page-edge); }
  .vscroll { left: 215px; top: 142px; width: 18px; height: 440px; background: #e9edf3;
    border-left: 1px solid #c3ccd8; border-right: 1px solid #c3ccd8; }
  .vscroll-thumb { left: 1px; top: 20px; width: 14px; height: 200px; border: 1px solid #a0adbe; border-radius: 2px;
    background: linear-gradient(90deg, #f4f7fb, #dce4ee); }

  .taskpane { left: 233px; top: 119px; width: 306px; height: 461px; background: var(--pane);
    border-left: 1px solid var(--pane-line); }
  .pane-title { left: 5px; top: 6px; font-size: 11px; white-space: nowrap; }
  .pane-toolbar { left: 2px; top: 26px; width: 300px; height: 18px; border-top: 1px solid #cfd7e2;
    background: linear-gradient(#f6f8fb, #e9eef4); }
  .url-label { left: 9px; top: 59px; font-size: 11px; }
  .url-field { left: 40px; top: 56px; width: 246px; height: 20px; background: #fff; border: 1px solid #a7b3c3;
    font-size: 10.5px; line-height: 18px; padding-left: 3px; white-space: nowrap; overflow: hidden; }
  .go-button { left: 228px; top: 84px; width: 57px; height: 19px; border: 1px solid #707070; border-radius: 3px;
    background: linear-gradient(#f2f2f2, #dcdcdc); font-size: 11px; text-align: center; line-height: 17px; }
  .key-tree { left: 20px; top: 131px; width: 265px; height: 221px; background: #fff; border: 1px solid #828790; }
  .key-tree text { font-family: "Noto Sans", sans-serif; font-size: 10.5px; fill: var(--text); }
  .key-tree .value { fill: var(--link-blue); }
</style>
</head>
<body>
<main class="stage">

  <header class="abs titlebar">
    <svg class="abs" style="left:500px;top:10px" width="36" height="20" viewBox="0 0 36 20" aria-label="Collapse ribbon and help">
      <polyline points="4,12 8,8 12,12" fill="none" stroke="#333" stroke-width="1.4"/>
      <circle cx="27" cy="10" r="8" fill="var(--help-blue)"/>
      <text x="27" y="14.5" text-anchor="middle" font-family="Noto Sans, sans-serif" font-weight="600" font-size="12" fill="#fff">?</text>
    </svg>
  </header>

  <section class="abs ribbon" aria-label="Ribbon">
    <div class="abs style-tile" style="left:-30px"><div class="style-sample sample-h1">AaBbCc</div><div class="style-name" style="text-align:right">Heading 1</div></div>
    <div class="abs style-tile" style="left:46px"><div class="style-sample sample-h2">AaBbCc</div><div class="style-name">Heading 2</div></div>
    <div class="abs style-tile" style="left:118px"><div class="style-sample sample-title">AaB</div><div class="style-name">Title</div></div>
    <div class="abs style-tile" style="left:190px"><div class="style-sample sample-subtitle">AaBbCc.</div><div class="style-name">Subtitle</div></div>
    <div class="abs style-tile" style="left:264px"><div class="style-sample sample-subtle">AaBbCcDc</div><div class="style-name">Subtle Em...</div></div>
    <div class="abs gallery-scroll">
      <svg width="14" height="56" viewBox="0 0 14 56"><path d="M4 11 L7 8 L10 11" fill="none" stroke="#444"/><path d="M4 27 L7 30 L10 27" fill="none" stroke="#444"/><line x1="0" y1="19" x2="14" y2="19" stroke="#b7c4d6"/><line x1="0" y1="38" x2="14" y2="38" stroke="#b7c4d6"/><line x1="4" y1="44" x2="10" y2="44" stroke="#444"/><path d="M4 47 L7 50 L10 47" fill="none" stroke="#444"/></svg>
    </div>

    <div class="abs" style="left:352px;top:6px;width:46px;text-align:center;font-size:11px;line-height:13px">
      <svg width="30" height="32" viewBox="0 0 30 32" aria-label="Change styles">
        <text x="15" y="26" text-anchor="middle" font-family="Caladea, serif" font-weight="700" font-size="30" fill="#6a5ccf">A</text>
      </svg>
      <div>Change</div><div>Styles ▾</div>
    </div>
    <div class="abs group-label" style="left:0;width:330px">Styles</div>
    <svg class="abs" style="left:386px;top:74px" width="8" height="8" viewBox="0 0 8 8"><path d="M1 1 H7 V7" fill="none" stroke="#6f7f96"/></svg>
    <div class="abs group-divider" style="left:402px"></div>

    <div class="abs edit-cmd" style="top:8px">
      <svg width="14" height="12" viewBox="0 0 14 12"><circle cx="4" cy="7" r="3" fill="none" stroke="#2b4f84" stroke-width="1.6"/><circle cx="10" cy="7" r="3" fill="none" stroke="#2b4f84" stroke-width="1.6"/></svg>Find ▾</div>
    <div class="abs edit-cmd" style="top:30px">
      <svg width="14" height="14" viewBox="0 0 14 14"><text x="0" y="6" font-size="6" fill="#333" font-family="Noto Sans, sans-serif">ab</text><text x="6" y="13" font-size="6" fill="#2b4f84" font-family="Noto Sans, sans-serif">ac</text><path d="M2 8 Q2 12 6 12" fill="none" stroke="#2b4f84"/></svg>Replace</div>
    <div class="abs edit-cmd" style="top:52px">
      <svg width="14" height="14" viewBox="0 0 14 14"><path d="M3 1 V12 L6 9 L8 13 L10 12 L8 8 H12 Z" fill="#fff" stroke="#333"/></svg>Select ▾</div>
    <div class="abs group-label" style="left:404px;width:72px">Editing</div>
    <div class="abs group-divider" style="left:477px"></div>
  </section>

  <div class="abs page" aria-label="Document page"></div>
  <svg class="abs" style="left:217px;top:126px" width="14" height="14" viewBox="0 0 14 14" aria-label="View ruler"><rect x="1.5" y="1.5" width="11" height="11" fill="#f4f6f9" stroke="#6f7c8d"/><path d="M4 5 H10 M4 8 H8" stroke="#6f7c8d"/></svg>
  <div class="abs vscroll">
    <svg class="abs" style="left:3px;top:6px" width="10" height="8" viewBox="0 0 10 8"><path d="M1 6 L5 2 L9 6 Z" fill="#555"/></svg>
    <div class="abs vscroll-thumb"><svg class="abs" style="left:3px;top:94px" width="8" height="8" viewBox="0 0 8 8"><path d="M0 1.5 H8 M0 4 H8 M0 6.5 H8" stroke="#6c7a8c"/></svg></div>
  </div>

  <aside class="abs taskpane" aria-label="Json To Doc Importer pane">
    <div class="abs pane-title">Json To Doc Importer.</div>
    <svg class="abs" style="left:278px;top:7px" width="26" height="12" viewBox="0 0 26 12"><path d="M1 3 H9 L5 8 Z" fill="#333"/><path d="M16 2 L24 10 M24 2 L16 10" stroke="#333" stroke-width="1.6"/></svg>
    <div class="abs pane-toolbar"><svg class="abs" style="left:3px;top:3px" width="4" height="12" viewBox="0 0 4 12"><path d="M2 1 V2 M2 5 V6 M2 9 V10" stroke="#7a8797" stroke-width="1.5"/></svg></div>

    <div class="abs url-label">URL</div>
    <div class="abs url-field">https://files.brightcrate.net/demo/test.json</div>
    <div class="abs go-button">Go</div>

    <div class="abs key-tree" aria-label="JSON keys">
      <svg width="263" height="219" viewBox="0 0 263 219">
        <g stroke="var(--tree-line)" stroke-dasharray="1 1" fill="none">
          <path d="M15 14 V154"/>
          <path d="M15 26 H29 M15 58 H29 M15 90 H29 M15 154 H29"/>
          <path d="M19 10 H25"/>
          <path d="M54 31 V42 H62"/>
          <path d="M54 63 V74 H62"/>
          <path d="M34 95 V138 M34 106 H48 M34 122 H48 M34 138 H48"/>
          <path d="M38 26 H43 M38 58 H43 M38 90 H43 M38 154 H43 M57 106 H61 M57 122 H61 M57 138 H61"/>
        </g>
        <g fill="#fff" stroke="#919191">
          <rect x="10.5" y="5.5" width="9" height="9"/>
          <rect x="29.5" y="21.5" width="9" height="9"/>
          <rect x="29.5" y="53.5" width="9" height="9"/>
          <rect x="29.5" y="85.5" width="9" height="9"/>
          <rect x="48.5" y="101.5" width="9" height="9"/>
          <rect x="48.5" y="117.5" width="9" height="9"/>
          <rect x="48.5" y="133.5" width="9" height="9"/>
          <rect x="29.5" y="149.5" width="9" height="9"/>
        </g>
        <g stroke="#222">
          <path d="M12.5 10 H17.5 M31.5 26 H36.5 M31.5 58 H36.5 M31.5 90 H36.5"/>
          <path d="M50.5 106 H55.5 M53 103.5 V108.5 M50.5 122 H55.5 M53 119.5 V124.5 M50.5 138 H55.5 M53 135.5 V140.5 M31.5 154 H36.5 M34 151.5 V156.5"/>
        </g>
        <text x="25" y="14">Root</text>
        <text x="44" y="30">name</text>
        <text class="value" x="63" y="46">Tom</text>
        <text x="44" y="62">address</text>
        <text class="value" x="63" y="78">45 Ledger Lane, Dorton</text>
        <text x="44" y="94">details</text>
        <text x="62" y="110">job</text>
        <text x="62" y="126">title</text>
        <text x="62" y="142">age</text>
        <text x="44" y="158">cars</text>
      </svg>
    </div>
  </aside>

</main>
</body>
</html>
```